Business Card Design Project

We need a double-sided business card design for our e-commerce company. Be as creative as you can.

Reason: Change of logo

Target Market(s)

Business owners

Industry/Entity Type

E-Commerce

Requirements
Must have
• Name (editable)
Mobile number -editable
www.trizvo.com - MUST STAND OUT ALONE
Office address:
27 Pellow Road
#09-04 Corbell Tower
Singapore 058214

```html
<!DOCTYPE html>
<html lang="en">
<head>
<meta charset="utf-8">
<title>Trizvo Business Card</title>
<link rel="stylesheet" href="https://fonts.googleapis.com/css2?family=Open+Sans:wght@400;600&family=PT+Sans+Narrow:wght@400&display=swap">
<style>
  :root {
    --page-bg: #ece9e4;
    --card-dark: #050505;
    --card-mid: #2a2a2a;
    --card-light: #4a4a4a;
    --brand-orange: #f07d1c;
    --contact-orange: #f29a1f;
    --web-red: #e8202a;
  }
  * { margin: 0; padding: 0; box-sizing: border-box; }
  html, body {
    width: 1200px;
    height: 1200px;
    overflow: hidden;
    background: var(--page-bg);
  }
  .canvas {
    position: relative;
    width: 1200px;
    height: 1200px;
  }
  .card {
    position: absolute;
    left: 160px;
    width: 896px;
    border-radius: 48px;
    overflow: hidden;
    background: var(--card-dark);
  }
  .card--front { top: 84px; height: 516px; }
  .card--back { top: 648px; height: 522px; }
  .card__pattern {
    position: absolute;
    inset: 0;
    background:
      linear-gradient(135deg, var(--card-light) 0%, var(--card-mid) 35%, var(--card-dark) 65%, var(--card-mid) 100%);
  }
  .brand-name {
    position: absolute;
    left: 0;
    right: 0;
    top: 150px;
    text-align: center;
    font-family: "Open Sans", sans-serif;
    font-weight: 600;
    font-size: 190px;
    line-height: 1;
    color: var(--brand-orange);
    letter-spacing: -2px;
  }
  .contact {
    position: absolute;
    color: var(--contact-orange);
    white-space: nowrap;
  }
  .contact__name {
    left: 69px;
    top: 120px;
    font-family: "PT Sans Narrow", sans-serif;
    font-size: 46px;
    line-height: 1;
  }
  .contact__mobile {
    left: 69px;
    top: 180px;
    font-family: "PT Sans Narrow", sans-serif;
    font-size: 38px;
    line-height: 1;
  }
  .contact__web {
    left: 69px;
    top: 218px;
    font-family: "Open Sans", sans-serif;
    font-size: 52px;
    line-height: 1.1;
    color: var(--web-red);
    letter-spacing: 1px;
  }
  .address {
    position: absolute;
    left: 418px;
    top: 290px;
    color: var(--contact-orange);
    font-family: "Open Sans", sans-serif;
    font-size: 33px;
    line-height: 44px;
    white-space: nowrap;
  }
  .address__label,
  .address__street,
  .address__city { letter-spacing: 2.5px; }
  .address__unit {
    font-family: "PT Sans Narrow", sans-serif;
    font-size: 38px;
  }
</style>
</head>
<body>
  <main class="canvas">
    <section class="card card--front">
      <div class="card__pattern" role="img" aria-label="Dark glossy faceted pyramid pattern"></div>
      <div class="brand-name">Trizvo</div>
    </section>

    <section class="card card--back">
      <div class="card__pattern" role="img" aria-label="Dark glossy faceted pyramid pattern"></div>
      <div class="contact contact__name">Name</div>
      <div class="contact contact__mobile">Mobile No</div>
      <div class="contact contact__web">www.trizvo.com</div>
      <address class="address" style="font-style: normal;">
        <div class="address__label">Office address:</div>
        <div class="address__street">27 Pellow Road</div>
        <div class="address__unit">#09-04 Corbell Tower</div>
        <div class="address__city">Singapore 058214</div>
      </address>
    </section>
  </main>
</body>
</html>
```